Website for IT consulting Company

I need a website upgrade, the existing site content is ok, I would also like to add a testimonial page, the site should be something that is easy for us to update content. You use the content from www.velmarketa.com as an example. I will also post update logo and artwork. I also need a contact form with some type of validation or captcha.

Please omit Address maps

Target Market(s)

small business, service oriented companies. We provide IT Consulting, support and mangement

Industry/Entity Type

Information Technology

Coding

Coded - Design and coding required

Number of Pages Required

1 page

Font styles to use
Serif
Sans Serif

Requirements
Must have
• Contain logo attached, and content from existing web site www.velmarketa.com.
• Also need to update content easily, and be movable to different platforms.
• There is a catch phrase
• "Let us worry about your technology…” “ so you don’t have to!”
• Should be included.
Nice to have
• Testimonial page, Project page where we can post new and past projects and pictures
Should not have
• none

```html
<!DOCTYPE html>
<html lang="en">
<head>
<meta charset="utf-8">
<title>Testimonial – Velmarketa</title>
<link href="https://fonts.googleapis.com/css2?family=Roboto:wght@400;500;700&display=swap" rel="stylesheet">
<style>
:root{
  --orange:#f1822b;
  --dark:#23222a;
  --text:#5d5d5d;
  --ink:#222;
  --white:#fff;
  --line:#ececec;
  --muted:#8b8a90;
}
*{box-sizing:border-box;margin:0;padding:0}
html,body{width:1030px;height:1200px;overflow:hidden}
body{font-family:'Roboto',sans-serif;background:var(--white);position:relative;color:var(--text)}
.hero{position:absolute;left:0;top:0;width:1030px;height:291px}
.hero-photo{position:absolute;inset:0;background:linear-gradient(100deg,#b9b9b9 0%,#8d8b89 30%,#6f6866 48%,#9a9896 62%,#d0d0cf 78%,#b5b5b5 100%)}
.hero-shade{position:absolute;inset:0;background:rgba(40,40,40,.18)}
.brand{position:absolute;left:76px;top:12px;display:flex;align-items:center;gap:8px;color:var(--white);font-size:24px;font-weight:700;letter-spacing:.5px}
.brand-mark{width:22px;height:22px;background:var(--orange)}
.nav{position:absolute;right:77px;top:21px;display:flex;gap:28px;align-items:center;font-size:12.5px;color:var(--white)}
.nav a{color:inherit;text-decoration:none;padding-bottom:3px}
.nav a.active{border-bottom:1px solid var(--white)}
.nav-rule{position:absolute;left:77px;right:77px;top:56px;height:1px;background:rgba(255,255,255,.35)}
.hero-title{position:absolute;left:0;right:0;top:141px;text-align:center;color:var(--white);font-size:31px;font-weight:700}
.crumbs{position:absolute;left:0;right:0;top:178px;text-align:center;color:var(--white);font-size:12.5px;word-spacing:3px}
.testimonials{position:absolute;left:78px;top:348px;width:874px;display:grid;grid-template-columns:repeat(3,283px);column-gap:12px;row-gap:93px}
.card{position:relative;height:131px;background:var(--white);border:1px solid #f0f0f0;box-shadow:0 1px 3px rgba(0,0,0,.1);border-radius:2px}
.card::after{content:"";position:absolute;left:36px;bottom:-7px;width:12px;height:12px;background:var(--white);transform:rotate(45deg);box-shadow:2px 2px 2px rgba(0,0,0,.06)}
.quote-icon{position:absolute;left:21px;top:37px}
.card p{position:absolute;left:51px;top:33px;right:16px;font-size:11.3px;line-height:17.6px;color:var(--text)}
.author{position:absolute;left:4px;top:150px;display:flex;align-items:center;gap:8px}
.avatar{width:54px;height:54px;border-radius:50%;border:3px solid var(--white);box-shadow:0 0 3px rgba(0,0,0,.2);background:linear-gradient(150deg,#d9cfc8,#8e7a6e 60%,#4a4140)}
.author-name{font-size:11.3px;color:var(--orange);line-height:13px}
.author-role{font-size:11px;color:var(--ink);line-height:13px}
.view-all{position:absolute;left:470px;top:797px;width:89px;height:30px;background:var(--orange);color:var(--white);font-size:11.5px;display:flex;align-items:center;justify-content:center;border-radius:2px}
.footer{position:absolute;left:0;top:880px;width:1030px;height:320px;background:var(--dark);color:var(--white)}
.foot-brand{position:absolute;left:76px;top:48px;display:flex;align-items:center;gap:9px;font-size:29px;font-weight:700;letter-spacing:.5px;color:#d8d8d8}
.foot-brand .brand-mark{width:28px;height:28px}
.about{position:absolute;left:76px;top:107px;width:260px;font-size:11.5px;line-height:17px}
.read-more{position:absolute;left:76px;top:166px;font-size:11.5px;display:flex;gap:6px;align-items:center}
.social{position:absolute;left:76px;top:202px;display:flex;gap:5px}
.social span{width:25px;height:25px;border-radius:50%;background:#34333b}
.social span:first-child{background:var(--orange)}
.col{position:absolute;top:52px}
.col h3{font-size:14.5px;font-weight:400;margin-bottom:20px;position:relative}
.col h3::after{content:"";position:absolute;left:0;bottom:-9px;width:22px;height:2px;background:#4a4951}
.col ul{list-style:none}
.col li{font-size:11.3px;line-height:23px;position:relative;padding-left:11px}
.col li::before{content:"";position:absolute;left:0;top:10px;width:3px;height:3px;border-radius:50%;background:var(--muted)}
.col.quick{left:394px}
.col.services{left:548px}
.col.contact{left:812px}
.contact-row{display:flex;gap:8px;font-size:11.3px;line-height:19px;margin-bottom:12px}
.contact-row svg{flex:none;margin-top:4px}
.copyright{position:absolute;left:0;right:0;top:290px;text-align:center;font-size:11.3px}
.to-top{position:absolute;left:977px;top:256px;width:30px;height:30px;border-radius:50%;background:var(--orange);display:flex;align-items:center;justify-content:center}
</style>
</head>
<body>

<header class="hero">
  <div class="hero-photo" role="img" aria-label="Photo of a bearded man in glasses and tie working at a desktop computer"></div>
  <div class="hero-shade"></div>
  <div class="brand"><span class="brand-mark"></span>VELMARKETA</div>
  <nav class="nav">
    <svg width="10" height="9" viewBox="0 0 10 9"><path d="M5 0 10 4.5H8.5V9H6V6H4V9H1.5V4.5H0Z" fill="#fff"/></svg>
    <a href="#">Contact</a><a href="#">Project</a><a href="#">Support</a><a href="#" class="active">Testimonial</a><a href="#">Clients</a><a href="#">Careers</a>
  </nav>
  <div class="nav-rule"></div>
  <h1 class="hero-title">TESTIMONIAL</h1>
  <div class="crumbs">Home | Testimonial</div>
</header>

<main class="testimonials">
  <div class="card"><svg class="quote-icon" width="21" height="16" viewBox="0 0 21 16"><path d="M0 0h8v9c0 4-2 6-6 7l-1-2c2-1 3-2 3-4H0Z M12 0h8v9c0 4-2 6-6 7l-1-2c2-1 3-2 3-4h-4Z" fill="#d5d5d5"/></svg><p>This is Photoshop's version of Lorem Ipsum Proin gravida nibh vel velit auctor aliquet. Aenean sollicitudin lorem quis bibendum auctor, nisi elit velit auctor aliquet...</p>
    <div class="author"><div class="avatar" role="img" aria-label="Portrait of client"></div><div><div class="author-name">Johny Doe</div><div class="author-role">CEO</div></div></div></div>
  <div class="card"><svg class="quote-icon" width="21" height="16" viewBox="0 0 21 16"><path d="M0 0h8v9c0 4-2 6-6 7l-1-2c2-1 3-2 3-4H0Z M12 0h8v9c0 4-2 6-6 7l-1-2c2-1 3-2 3-4h-4Z" fill="#d5d5d5"/></svg><p>This is Photoshop's version of Lorem Ipsum Proin gravida nibh vel velit auctor aliquet. Aenean sollicitudin lorem quis bibendum auctor, nisi elit velit auctor aliquet...</p>
    <div class="author"><div class="avatar" role="img" aria-label="Portrait of client"></div><div><div class="author-name">Renaud Castell</div><div class="author-role">CEO</div></div></div></div>
  <div class="card"><svg class="quote-icon" width="21" height="16" viewBox="0 0 21 16"><path d="M0 0h8v9c0 4-2 6-6 7l-1-2c2-1 3-2 3-4H0Z M12 0h8v9c0 4-2 6-6 7l-1-2c2-1 3-2 3-4h-4Z" fill="#d5d5d5"/></svg><p>This is Photoshop's version of Lorem Ipsum Proin gravida nibh vel velit auctor aliquet. Aenean sollicitudin lorem quis bibendum auctor, nisi elit velit auctor aliquet...</p>
    <div class="author"><div class="avatar" role="img" aria-label="Portrait of client"></div><div><div class="author-name">Stella Janes</div><div class="author-role">CEO</div></div></div></div>
  <div class="card"><svg class="quote-icon" width="21" height="16" viewBox="0 0 21 16"><path d="M0 0h8v9c0 4-2 6-6 7l-1-2c2-1 3-2 3-4H0Z M12 0h8v9c0 4-2 6-6 7l-1-2c2-1 3-2 3-4h-4Z" fill="#d5d5d5"/></svg><p>This is Photoshop's version of Lorem Ipsum Proin gravida nibh vel velit auctor aliquet. Aenean sollicitudin lorem quis bibendum auctor, nisi elit velit auctor aliquet...</p>
    <div class="author"><div class="avatar" role="img" aria-label="Portrait of client"></div><div><div class="author-name">Tarek Zorin</div><div class="author-role">CEO</div></div></div></div>
  <div class="card"><svg class="quote-icon" width="21" height="16" viewBox="0 0 21 16"><path d="M0 0h8v9c0 4-2 6-6 7l-1-2c2-1 3-2 3-4H0Z M12 0h8v9c0 4-2 6-6 7l-1-2c2-1 3-2 3-4h-4Z" fill="#d5d5d5"/></svg><p>This is Photoshop's version of Lorem Ipsum Proin gravida nibh vel velit auctor aliquet. Aenean sollicitudin lorem quis bibendum auctor, nisi elit velit auctor aliquet...</p>
    <div class="author"><div class="avatar" role="img" aria-label="Portrait of client"></div><div><div class="author-name">Michel Pardieu</div><div class="author-role">CEO</div></div></div></div>
  <div class="card"><svg class="quote-icon" width="21" height="16" viewBox="0 0 21 16"><path d="M0 0h8v9c0 4-2 6-6 7l-1-2c2-1 3-2 3-4H0Z M12 0h8v9c0 4-2 6-6 7l-1-2c2-1 3-2 3-4h-4Z" fill="#d5d5d5"/></svg><p>This is Photoshop's version of Lorem Ipsum Proin gravida nibh vel velit auctor aliquet. Aenean sollicitudin lorem quis bibendum auctor, nisi elit velit auctor aliquet...</p>
    <div class="author"><div class="avatar" role="img" aria-label="Portrait of client"></div><div><div class="author-name">Brent Galloway</div><div class="author-role">CEO</div></div></div></div>
</main>

<div class="view-all">View All</div>

<footer class="footer">
  <div class="foot-brand"><span class="brand-mark"></span>VELMARKETA</div>
  <p class="about">Outsourcing is subcontracting a process, such as product design or manufacturing, to a third-party company.[1] The decision ...</p>
  <div class="read-more">Read More <svg width="11" height="7" viewBox="0 0 11 7"><path d="M0 3.5h10M7 .5l3 3-3 3" stroke="#fff" fill="none"/></svg></div>
  <div class="social"><span></span><span></span><span></span><span></span></div>

  <div class="col quick"><h3>QuickLinks</h3>
    <ul><li>Home</li><li>Contact</li><li>Project</li><li>Support</li><li>Testimonial</li><li>Clients</li><li>Careers</li></ul></div>
  <div class="col services"><h3>Our Services</h3>
    <ul><li>Managed IT Solutions</li><li>Remote Diagnostic And Support</li><li>IT Infrastrucrture Design and Installation</li></ul></div>
  <div class="col contact"><h3>Contact Informatiom</h3>
    <div class="contact-row"><svg width="8" height="11" viewBox="0 0 8 11"><path d="M4 0a4 4 0 0 1 4 4c0 3-4 7-4 7S0 7 0 4a4 4 0 0 1 4-4Zm0 2.5a1.5 1.5 0 1 0 0 3 1.5 1.5 0 0 0 0-3Z" fill="var(--orange)"/></svg><span>Address: Line goes here,<br>city name country name</span></div>
    <div class="contact-row"><svg width="9" height="9" viewBox="0 0 9 9"><path d="M1 0h2l1 2-1.2 1.2a5 5 0 0 0 3 3L7 5l2 1v2a1 1 0 0 1-1 1A8 8 0 0 1 0 1a1 1 0 0 1 1-1Z" fill="var(--orange)"/></svg><span>Phone: 123 456 7890</span></div>
    <div class="contact-row"><svg width="10" height="8" viewBox="0 0 10 8"><rect width="10" height="8" fill="var(--orange)"/><path d="M0 0l5 4 5-4" stroke="var(--dark)" fill="none"/></svg><span>Email: info@example.com</span></div>
  </div>

  <div class="to-top"><svg width="8" height="5" viewBox="0 0 8 5"><path d="M1 4l3-3 3 3" stroke="#fff" stroke-width="1.4" fill="none"/></svg></div>
  <div class="copyright">Copyright © 2017 - Velmarketa Development Group, Inc - All rights reserved</div>
</footer>

</body>
</html>
```